Letterhead and Business card for Construction company

We need a letterhead and business card with our new company logo. We are based in NY. We develop and build properties.

The design should incorporate some unique feature from the logo (shape, font...). it should look like an extension from it.

Design should be clean and elegant, professional, not too busy.

The letterhead should include:
Logo (attached)
Address
Phone
Email

Please find the attached logo images and AI file.

Target Market(s)

Construction industry professionals

Industry/Entity Type

Construction, Development

Font styles to use
Sans Serif

Colors

Designer to choose colors to be used in the design.

Requirements
Must have
• Design should incorporate logo elements, additional assets are welcome. I'd like to see some other shapes / images invorporated too.

```html
<!DOCTYPE html>
<html lang="en">
<head>
<meta charset="utf-8">
<title>Halvern Builders — Stationery</title>
<link rel="stylesheet" href="https://fonts.googleapis.com/css2?family=Montserrat:wght@400;500;600;700;800&display=swap">
<style>
  :root{
    --bg:#e4e5e7;
    --paper:#ffffff;
    --ink:#1d1d1f;
    --text:#555a60;
    --muted:#8a8f95;
    --accent:#f47b20;
  }
  *{box-sizing:border-box;margin:0;padding:0}
  html,body{width:690px;height:1200px;overflow:hidden}
  body{background:var(--bg);font-family:"Montserrat",Arial,sans-serif;color:var(--text);position:relative}

  /* Brand lockup */
  .brand{display:flex;align-items:center;gap:7px}
  .brand-square{width:16px;height:16px;background:var(--accent);flex:none}
  .brand-name{font-weight:800;color:var(--ink);text-transform:uppercase;line-height:1.05;letter-spacing:.04em}
  .brand-name span{display:block}

  /* Letterhead */
  .letterhead{position:absolute;left:125px;top:30px;width:440px;height:622px;background:var(--paper);
    box-shadow:0 2px 10px rgba(0,0,0,.12)}
  .letterhead .brand{position:absolute;left:32px;top:42px}
  .letterhead .brand-name{font-size:15px}
  .sender{position:absolute;right:34px;top:36px;font-size:6.5px;line-height:1.55;color:var(--text)}
  .sender .addr{margin-bottom:3px}
  .sender .line{display:flex;align-items:center;gap:5px}
  .icon{width:7px;height:7px;flex:none}
  .letter{position:absolute;left:32px;top:150px;width:376px}
  .letter .date{font-size:7.5px;margin-bottom:4px}
  .letter .recipient{font-size:14px;font-weight:800;color:var(--ink);letter-spacing:.02em}
  .letter .role{font-size:7.5px;color:var(--muted);margin-bottom:16px}
  .letter p{font-size:6.6px;line-height:1.65;margin-bottom:10px;text-align:justify}
  .letter .closing{margin-top:6px}
  .signature{width:34px;height:12px;margin-top:8px;border-radius:6px;
    background:linear-gradient(90deg,rgba(244,123,32,.75),rgba(244,123,32,.35))}
  .letter-footer{position:absolute;left:0;bottom:0;width:440px;height:10px}

  /* Business cards */
  .card{position:absolute;left:330px;width:250px;height:142px;box-shadow:0 2px 8px rgba(0,0,0,.15);overflow:hidden}
  .card-front{top:880px;background:var(--paper)}
  .card-back{top:1040px;background:var(--ink)}
  .card-front .brand{position:absolute;left:18px;top:54px;gap:5px}
  .card-front .brand-square{width:11px;height:11px}
  .card-front .brand-name{font-size:10px}
  .card-divider{position:absolute;left:124px;top:26px;width:1px;height:86px;background:#d6d8db}
  .holder{position:absolute;left:136px;top:30px;font-size:5.6px;line-height:1.6}
  .holder .name{font-size:9px;font-weight:800;color:var(--accent);letter-spacing:.03em;line-height:1.2}
  .holder .title{color:var(--muted);margin-bottom:5px}
  .holder .line{display:flex;align-items:center;gap:4px}
  .holder .icon{width:5.5px;height:5.5px}
  .card-corner{position:absolute;right:0;bottom:0;width:250px;height:14px}
  .card-back .brand{position:absolute;left:50%;top:50%;transform:translate(-50%,-50%);gap:8px}
  .card-back .brand-square{width:18px;height:18px}
  .card-back .brand-name{color:#fff;font-size:17px}
</style>
</head>
<body>

<svg width="0" height="0" style="position:absolute">
  <defs>
    <symbol id="i-pin" viewBox="0 0 10 10"><path d="M5 0.5a3.3 3.3 0 0 0-3.3 3.3C1.7 6.3 5 9.5 5 9.5s3.3-3.2 3.3-5.7A3.3 3.3 0 0 0 5 .5zm0 4.6a1.3 1.3 0 1 1 0-2.6 1.3 1.3 0 0 1 0 2.6z" fill="#f47b20"/></symbol>
    <symbol id="i-phone" viewBox="0 0 10 10"><path d="M2.2.8l1.6 2-1 1.1a6 6 0 0 0 3.3 3.3l1.1-1 2 1.6-.9 1.6C4.7 9.2.8 5.3.6 1.7z" fill="#f47b20"/></symbol>
    <symbol id="i-mail" viewBox="0 0 10 10"><rect x=".5" y="2" width="9" height="6" rx=".6" fill="#f47b20"/><path d="M1 2.6l4 3 4-3" stroke="#fff" stroke-width=".8" fill="none"/></symbol>
    <symbol id="i-web" viewBox="0 0 10 10"><circle cx="5" cy="5" r="4.3" fill="#f47b20"/><path d="M.8 5h8.4M5 .7c-2.4 2.6-2.4 6 0 8.6M5 .7c2.4 2.6 2.4 6 0 8.6" stroke="#fff" stroke-width=".6" fill="none"/></symbol>
  </defs>
</svg>

<section class="letterhead">
  <div class="brand">
    <div class="brand-square"></div>
    <div class="brand-name"><span>Halvern</span><span>Builders</span></div>
  </div>

  <div class="sender">
    <div class="line addr"><svg class="icon"><use href="#i-pin"/></svg><div>48 Harbor Street<br>Brooklyn, NY 11201</div></div>
    <div class="line"><svg class="icon"><use href="#i-phone"/></svg>(212) 555-0148</div>
    <div class="line"><svg class="icon"><use href="#i-mail"/></svg>info@halvernbuilders.com</div>
    <div class="line"><svg class="icon"><use href="#i-web"/></svg>www.halvernbuilders.com</div>
  </div>

  <article class="letter">
    <div class="date">01 December, 2023</div>
    <div class="recipient">DANIEL REYES</div>
    <div class="role">Chief Executive Officer</div>
    <p>Our team plans, develops and builds residential and commercial properties across New York. Every project begins with a clear schedule, honest budgets and close contact with the owner. We manage permits, site work, structure and finishes so each building is delivered safely, on time and to a standard we are proud to sign.</p>
    <p>Thank you for considering us for your upcoming development. Attached you will find our proposal, an outline of the phases and the key dates we discussed during our meeting last week. Please review the details at your convenience.</p>
    <p>Should you have any questions about scope, materials or timing, our project office is ready to help. We look forward to building something lasting together and to a partnership that serves your goals for years to come.</p>
    <p class="closing">Best Regards,</p>
    <div class="signature" role="img" aria-label="Handwritten signature"></div>
  </article>

  <svg class="letter-footer" viewBox="0 0 440 10" preserveAspectRatio="none">
    <rect x="0" y="3" width="440" height="7" fill="#1d1d1f"/>
    <polygon points="318,10 328,0 440,0 440,10" fill="#f47b20"/>
    <polygon points="330,10 337,3 440,3 440,10" fill="#1d1d1f"/>
  </svg>
</section>

<section class="card card-front">
  <div class="brand">
    <div class="brand-square"></div>
    <div class="brand-name"><span>Halvern</span><span>Builders</span></div>
  </div>
  <div class="card-divider"></div>
  <div class="holder">
    <div class="name">OWEN CARTER</div>
    <div class="title">Founder</div>
    <div class="line"><svg class="icon"><use href="#i-pin"/></svg>48 Harbor Street</div>
    <div class="line"><svg class="icon"><use href="#i-pin"/></svg>Brooklyn, NY 11201</div>
    <div class="line"><svg class="icon"><use href="#i-phone"/></svg>(212) 555-0148</div>
    <div class="line"><svg class="icon"><use href="#i-mail"/></svg>info@halvernbuilders.com</div>
    <div class="line"><svg class="icon"><use href="#i-web"/></svg>www.halvernbuilders.com</div>
  </div>
  <svg class="card-corner" viewBox="0 0 250 14" preserveAspectRatio="none">
    <polygon points="150,14 160,4 250,4 250,14" fill="#1d1d1f"/>
    <polygon points="190,14 204,0 250,0 250,6 210,6 202,14" fill="#f47b20"/>
  </svg>
</section>

<section class="card card-back">
  <div class="brand">
    <div class="brand-square"></div>
    <div class="brand-name"><span>Halvern</span><span>Builders</span></div>
  </div>
</section>

</body>
</html>
```